Multi brand diverse distributor requires new business card

We're a distributor representing multiple brands and would like a new business card reflecting our diversity.

We incorporate landscape architecture, environmental engineering and sustainability into construction projects.

KV Group is the company name, and therefore the KV logo should be the primary logo.

Target Market(s)

Engineers, Landscape Architects, Environmental

Contact Information for Business Card

See sample

Colors

Designer to choose colors to be used in the design.

```html
<!DOCTYPE html>
<html lang="en">
<head>
<meta charset="utf-8">
<title>KV Group business card</title>
<link rel="stylesheet" href="https://fonts.googleapis.com/css2?family=Roboto:wght@400;500;700&display=swap">
<style>
  :root {
    --red: #c41e3a;
    --red-dark: #a8172f;
    --white: #ffffff;
    --ink: #3a3a3a;
    --grey: #7b7b7b;
    --partner-dot: #b9b9b9;
    --stage: #e6e6e8;
  }
  * { box-sizing: border-box; margin: 0; padding: 0; }
  html, body { width: 1200px; height: 780px; overflow: hidden; }
  body {
    background: var(--stage);
    font-family: "Roboto", Arial, sans-serif;
    display: flex;
    align-items: center;
    justify-content: center;
    gap: 40px;
  }
  .card {
    width: 520px;
    height: 300px;
    border-radius: 16px;
    overflow: hidden;
    position: relative;
    background: var(--white);
    box-shadow: 0 6px 18px rgba(0,0,0,0.15);
  }

  /* Company name set as plain text with one square */
  .company-name {
    display: flex;
    align-items: center;
    gap: 12px;
    font-family: "Roboto", Arial, sans-serif;
    font-weight: 700;
    line-height: 1;
    white-space: nowrap;
  }
  .company-name__square { display: block; background: currentColor; }
  .company-name--light { color: var(--white); font-size: 48px; }
  .company-name--light .company-name__square { width: 26px; height: 26px; }
  .company-name--red { color: var(--red); font-size: 32px; }
  .company-name--red .company-name__square { width: 18px; height: 18px; }

  /* Brand face */
  .card--brands .brand-field {
    position: absolute; inset: 0 0 84px 0;
    background: linear-gradient(135deg, var(--red) 0%, var(--red-dark) 100%);
    display: flex; align-items: center; justify-content: center;
  }
  .partners {
    position: absolute; left: 0; right: 0; bottom: 0; height: 84px;
    display: flex; align-items: center; justify-content: space-around;
    padding: 0 18px;
  }
  .partner {
    display: flex; align-items: center; gap: 6px;
    font-size: 13px; font-weight: 700; color: var(--grey);
  }
  .partner__mark { width: 14px; height: 14px; border-radius: 50%; background: var(--partner-dot); }

  /* Contact face */
  .contact { position: absolute; left: 30px; top: 28px; }
  .contact__name { color: var(--red); font-weight: 700; font-size: 19px; }
  .contact__role { color: var(--ink); font-size: 12px; margin-top: 3px; }
  .contact__list { list-style: none; margin-top: 20px; font-size: 12px; color: var(--ink); }
  .contact__list li { display: flex; align-items: center; gap: 8px; height: 18px; }
  .contact__list li.gap { margin-top: 10px; }
  .contact__list svg { width: 11px; height: 11px; fill: var(--red); }
  .card--contact .company-name { position: absolute; right: 40px; top: 124px; }
  .offices {
    position: absolute; left: 0; right: 0; bottom: 0; height: 62px;
    background: var(--red);
    color: var(--white);
    font-size: 13px; letter-spacing: 0.5px;
    display: flex; align-items: center; padding-left: 30px;
  }
</style>
</head>
<body>

  <section class="card card--brands" aria-label="Card front">
    <div class="brand-field">
      <div class="company-name company-name--light">
        <span class="company-name__square"></span>KV Group
      </div>
    </div>
    <div class="partners">
      <span class="partner"><span class="partner__mark"></span>Timbrel</span>
      <span class="partner"><span class="partner__mark"></span>Arcline</span>
      <span class="partner"><span class="partner__mark"></span>Parkbench Co</span>
      <span class="partner"><span class="partner__mark"></span>Aquafield</span>
    </div>
  </section>

  <section class="card card--contact" aria-label="Card back">
    <div class="contact">
      <h1 class="contact__name">Marco Delvecchi</h1>
      <p class="contact__role">B.Eng (Civil)</p>
      <ul class="contact__list">
        <li><svg viewBox="0 0 10 10"><rect x="2.5" y="0" width="5" height="10" rx="1"/></svg>0400 218 374</li>
        <li><svg viewBox="0 0 10 10"><rect x="0" y="3" width="10" height="7" rx="1"/><rect x="2" y="0" width="6" height="3"/></svg>1300 552 906</li>
        <li class="gap"><svg viewBox="0 0 10 10"><rect x="0" y="2" width="10" height="6" rx="1"/></svg>marco@kvgroup.com.au</li>
        <li><svg viewBox="0 0 10 10"><circle cx="5" cy="5" r="5"/></svg>www.kvgroup.com.au</li>
      </ul>
    </div>
    <div class="company-name company-name--red">
      <span class="company-name__square"></span>KV Group
    </div>
    <div class="offices">Adelaide | Brisbane | Melbourne | Perth | Sydney</div>
  </section>

</body>
</html>
```